Qorvane Management LLC Business Card

The sample logo was attached for the business Card Design for Traffic Control Company named Qorvane Management LLC. Card design needs to have the company logo and colors match the logo color. It will be nice to show some images of Traffic control signs or cones, even roads closer that math the company services

Target Market(s)

Temporary traffic control. Road closer.

Industry/Entity Type

Construction

Contact Information for Business Card

basic information, name, job title, address, email phone, website

Font styles to use
Serif
Sans Serif

Colors
F0912C
F2A743
F7CA91
FBE8D2
FDF5EE
EE7325
F08F49
F5BC92
FAE3D3
FDF4ED

```html
<!DOCTYPE html>
<html lang="en">
<head>
<meta charset="utf-8">
<title>Qorvane Management LLC – Business Card</title>
<link rel="stylesheet" href="https://fonts.googleapis.com/css2?family=Montserrat:wght@400;700&family=Archivo:wght@600;700;800&display=swap">
<style>
  :root {
    --brand-orange: #ff5323;
    --card-light: #f4f7f6;
    --ink: #2f3537;
    --page: #ffffff;
    --white: #ffffff;
  }
  * { box-sizing: border-box; margin: 0; padding: 0; }
  html, body { width: 1085px; height: 1200px; overflow: hidden; background: var(--page); }
  .canvas { position: relative; width: 1085px; height: 1200px; }

  .card {
    position: absolute;
    left: 132px;
    width: 818px;
    height: 467px;
    border-radius: 24px;
    overflow: hidden;
  }
  .card--front { top: 84px; background: var(--brand-orange); }
  .card--back { top: 644px; background: var(--card-light); border: 1px solid #e6eaea; }

  .wordmark { position: absolute; font-family: "Montserrat", sans-serif; font-weight: 700; text-align: center; }
  .wordmark__name { display: block; letter-spacing: 2px; line-height: 1; }
  .wordmark__suffix { display: block; letter-spacing: 3px; line-height: 1; }

  .card--front .wordmark { left: 0; right: 0; top: 158px; color: var(--white); }
  .card--front .wordmark__name { font-size: 86px; }
  .card--front .wordmark__suffix { font-size: 34px; margin-top: 24px; }

  .card--back .wordmark { left: 58px; width: 290px; top: 180px; color: var(--brand-orange); }
  .card--back .wordmark__name { font-size: 60px; }
  .card--back .wordmark__suffix { font-size: 24px; margin-top: 14px; letter-spacing: 2px; }

  .divider {
    position: absolute; left: 404px; top: 82px;
    width: 2px; height: 306px; background: var(--brand-orange);
  }

  .person { position: absolute; left: 441px; top: 104px; font-family: "Archivo", sans-serif; }
  .person__name { font-size: 27px; font-weight: 800; color: var(--brand-orange); letter-spacing: 2.5px; line-height: 1; }
  .person__title { font-size: 15px; font-weight: 700; color: var(--ink); letter-spacing: 1.5px; margin-top: 6px; }

  .contacts { position: absolute; left: 441px; top: 216px; list-style: none; font-family: "Archivo", sans-serif; }
  .contacts__item {
    display: flex; align-items: flex-start; gap: 14px;
    font-size: 16px; font-weight: 600; color: var(--ink);
    letter-spacing: 1.6px; line-height: 19px; margin-bottom: 14px;
  }
  .contacts__icon { width: 18px; height: 18px; flex: none; margin-top: 1px; }
  .contacts__icon * { fill: none; stroke: var(--ink); stroke-width: 1.4; stroke-linecap: round; stroke-linejoin: round; }
</style>
</head>
<body>
<main class="canvas">

  <section class="card card--front" aria-label="Card front">
    <div class="wordmark">
      <span class="wordmark__name">QORVANE</span>
      <span class="wordmark__suffix">MANAGEMENT LLC</span>
    </div>
  </section>

  <section class="card card--back" aria-label="Card back">
    <div class="wordmark">
      <span class="wordmark__name">QORVANE</span>
      <span class="wordmark__suffix">MANAGEMENT LLC</span>
    </div>

    <div class="divider"></div>

    <div class="person">
      <p class="person__name">Dario Whitfield</p>
      <p class="person__title">Manager</p>
    </div>

    <ul class="contacts">
      <li class="contacts__item">
        <svg class="contacts__icon" viewBox="0 0 18 18" aria-hidden="true">
          <path d="M4 2l3 3-1.5 2a10 10 0 0 0 5.5 5.5L13 11l3 3-2 2C8 16 2 10 2 4z"/>
          <path d="M10.5 2.5a5 5 0 0 1 5 5M10.5 5.5a2 2 0 0 1 2 2"/>
        </svg>
        <span>555-204-7816</span>
      </li>
      <li class="contacts__item">
        <svg class="contacts__icon" viewBox="0 0 18 18" aria-hidden="true">
          <rect x="1.5" y="4" width="15" height="10"/>
          <path d="M1.5 4l7.5 6 7.5-6M1.5 14l5.5-5M16.5 14l-5.5-5"/>
        </svg>
        <span>hello@qorvane.com</span>
      </li>
      <li class="contacts__item">
        <svg class="contacts__icon" viewBox="0 0 18 18" aria-hidden="true">
          <circle cx="9" cy="9" r="7.5"/>
          <ellipse cx="9" cy="9" rx="3.2" ry="7.5"/>
          <path d="M1.5 9h15M2.6 5.2h12.8M2.6 12.8h12.8"/>
        </svg>
        <span>www.qorvane.com</span>
      </li>
      <li class="contacts__item">
        <svg class="contacts__icon" viewBox="0 0 18 18" aria-hidden="true">
          <path d="M9 13s-4.5-4.2-4.5-7.5a4.5 4.5 0 0 1 9 0C13.5 8.8 9 13 9 13z"/>
          <circle cx="9" cy="5.5" r="1.6"/>
          <path d="M5 12.5c-2 .5-3 1.2-3 2 0 1.2 3.1 2 7 2s7-.8 7-2c0-.8-1-1.5-3-2"/>
        </svg>
        <span>418 Larkmoor Way 110 Your Location<br>Fairbrook, CA 95140</span>
      </li>
    </ul>
  </section>

</main>
</body>
</html>
```